Standard logo business card

We are seeking a solid, somewhat understated professional design. We are a tech company. We like fonts similar to Aptifer Slab. Front side will be white with the contact information and a small version of our primary (Light background) logo.

(We have three people so we will have three names and titles)

Back side will hold our reverse logo on dark background along with the tagline:

"Intelligent annotation solutions for complex data"

Target Market(s)

Professionals, Tech

Industry/Entity Type

Business

Contact Information for Business Card

Name
Title

Phone
Email
City, State
Website

[We will email leading designer specific contact information)

Font styles to use
Serif

Requirements
Must have
• Colors are:
• Orange RGB 245,92,23
• Blue RGB 3,34,56
Nice to have
• We like a split with the Name and Title on the right and then contact details (below) on the left.

```html
<!DOCTYPE html>
<html lang="en">
<head>
<meta charset="utf-8">
<title>Nortiva – Business Card</title>
<link rel="stylesheet" href="https://fonts.googleapis.com/css2?family=PT+Sans+Narrow:wght@400;700&display=swap">
<style>
  :root {
    --orange: rgb(245, 92, 23);
    --navy: rgb(3, 34, 56);
    --card-navy: #10243a;
    --white: #ffffff;
    --ink: #111822;
    --rule-grey: #8a8f96;
    --mark-brown: #6a3b30;
    --mark-grey: #4c5261;
    --shadow: rgba(0, 0, 0, 0.55);
  }
  * { box-sizing: border-box; margin: 0; padding: 0; }
  html, body { width: 1098px; height: 1200px; overflow: hidden; background: var(--white); }
  body { position: relative; font-family: "PT Sans Narrow", sans-serif; color: var(--ink); }

  .card { position: absolute; left: 80px; width: 960px; }
  .card-front {
    top: 24px; height: 520px; background: var(--white);
    box-shadow: 18px 20px 22px var(--shadow);
  }
  .card-back {
    top: 664px; height: 532px; background: var(--card-navy);
    box-shadow: 20px 8px 20px var(--shadow);
  }

  /* Front */
  .brand-small { position: absolute; left: 20px; top: 20px; display: flex; align-items: center; gap: 8px; }
  .brand-small .brand-square { width: 34px; height: 34px; background: var(--orange); }
  .brand-small .brand-name { font-size: 46px; font-weight: 700; color: var(--navy); line-height: 1; letter-spacing: -1px; }

  .person { position: absolute; left: 314px; width: 130px; text-align: center; }
  .person .person-name { font-size: 27px; line-height: 1; padding-bottom: 4px; border-bottom: 1px solid var(--rule-grey); }
  .person .person-role { font-size: 17px; font-weight: 700; margin-top: 4px; text-align: left; padding-left: 14px; }
  .person-1 { top: 92px; }
  .person-2 { top: 168px; }
  .person-3 { top: 262px; }
  .person-2 .person-role { padding-left: 22px; margin-top: 16px; }

  .divider { position: absolute; left: 524px; top: 86px; width: 2px; height: 240px; background: var(--orange); }

  .contact-number { position: absolute; font-size: 22px; font-weight: 700; }
  .contact-1 { left: 576px; top: 100px; }
  .contact-2 { left: 584px; top: 176px; }
  .contact-3 { left: 584px; top: 272px; }

  .info-band {
    position: absolute; left: 20px; top: 354px; width: 912px; height: 146px;
    background: var(--card-navy); color: var(--white);
  }
  .info-band svg { position: absolute; display: block; }
  .info-item { position: absolute; font-size: 30px; line-height: 1; }
  .info-phone { left: 110px; top: 34px; }
  .info-office { left: 110px; top: 96px; }
  .info-web { left: 650px; top: 34px; }
  .info-email { left: 650px; top: 96px; }
  .icon-home { left: 22px; top: 30px; }
  .icon-handset { left: 22px; top: 92px; }
  .icon-globe { left: 536px; top: 20px; }
  .icon-mail { left: 536px; top: 94px; }

  /* Back */
  .brand-large { position: absolute; left: 110px; top: 32px; display: flex; align-items: center; gap: 30px; }
  .brand-large .brand-square { width: 150px; height: 150px; background: var(--mark-brown); margin-top: 40px; }
  .brand-large .brand-name { font-size: 210px; font-weight: 700; color: var(--mark-grey); line-height: 1; letter-spacing: -4px; }

  .tagline {
    position: absolute; left: 0; width: 924px; top: 264px; text-align: center;
    font-size: 48px; color: var(--white);
  }
  .back-bar { position: absolute; left: 20px; top: 476px; width: 912px; height: 24px; background: var(--white); }
</style>
</head>
<body>

<section class="card card-front">
  <div class="brand-small">
    <span class="brand-square"></span>
    <span class="brand-name">Nortiva</span>
  </div>

  <div class="person person-1"><p class="person-name">Name</p><p class="person-role">position</p></div>
  <div class="person person-2"><p class="person-name">Name</p><p class="person-role">position</p></div>
  <div class="person person-3"><p class="person-name">Name</p><p class="person-role">position</p></div>

  <div class="divider"></div>

  <p class="contact-number contact-1">contact number</p>
  <p class="contact-number contact-2">contact number</p>
  <p class="contact-number contact-3">contact number</p>

  <div class="info-band">
    <svg class="icon-home" width="54" height="34" viewBox="0 0 54 34" aria-hidden="true">
      <path d="M27 2 L2 20 L8 20 L8 32 L22 32 L22 24 L32 24 L32 32 L46 32 L46 20 L52 20 Z" fill="#fff"/>
    </svg>
    <svg class="icon-handset" width="56" height="40" viewBox="0 0 56 40" aria-hidden="true">
      <path d="M4 30 C2 26 8 22 12 25 L16 28 C26 26 34 20 38 12 L35 8 C33 4 38 1 42 3 L52 8 C55 11 53 16 48 21 C38 31 24 38 10 37 C7 36 5 33 4 30 Z" fill="#fff"/>
    </svg>
    <svg class="icon-globe" width="60" height="52" viewBox="0 0 58 50" aria-hidden="true">
      <rect x="2" y="2" width="54" height="46" fill="none" stroke="#fff" stroke-width="2"/>
      <circle cx="29" cy="25" r="16" fill="none" stroke="#fff" stroke-width="2"/>
      <ellipse cx="29" cy="25" rx="7" ry="16" fill="none" stroke="#fff" stroke-width="2"/>
      <line x1="13" y1="25" x2="45" y2="25" stroke="#fff" stroke-width="2"/>
      <line x1="16" y1="17" x2="42" y2="17" stroke="#fff" stroke-width="2"/>
      <line x1="16" y1="33" x2="42" y2="33" stroke="#fff" stroke-width="2"/>
    </svg>
    <svg class="icon-mail" width="54" height="36" viewBox="0 0 54 36" aria-hidden="true">
      <rect x="2" y="2" width="50" height="32" fill="none" stroke="#fff" stroke-width="3"/>
      <path d="M2 2 L27 20 L52 2 M2 34 L20 16 M52 34 L34 16" fill="none" stroke="#fff" stroke-width="3"/>
    </svg>
    <p class="info-item info-phone">Phone number:</p>
    <p class="info-item info-office">Office location:</p>
    <p class="info-item info-web">Website:</p>
    <p class="info-item info-email">Email address:</p>
  </div>
</section>

<section class="card card-back">
  <div class="brand-large">
    <span class="brand-square"></span>
    <span class="brand-name">Nortiva</span>
  </div>
  <p class="tagline">"Intelligent annotation solutions for complex data"</p>
  <div class="back-bar"></div>
</section>

</body>
</html>
```